Business card design needed

My company does everything from wiring up your exisiting entertainment system, to installing a complete new system for you. We can mount your plasma on the wall, install an aerial point for you, setup some surround sound in your outdoor area or install a new cinema room in your house. Any Audio or Visual requirements you may have we can provide these for you. If you want to have a party to remember at your place or just some chilled sounds by the pool, we can give you just the right size system.

Industry/Entity Type

Entertainment

Contact Information for Business Card

The Sound Crew
Declan Whitford
e| declan@thesoundcrewqz.com.au
w| www.thesoundcrewqz.com.au
m| 0412 576 018

Requirements
Must have
• The logo that i have uploaded is just a starter...something similar to this but not exact or any new suggestions you have would be great too. Colour choice we are pretty easy on we did think Red and Yellow but happy to take advice, something that stands out from the rest i guess.

```html
<!DOCTYPE html>
<html lang="en">
<head>
<meta charset="utf-8">
<title>The Sound Crew – Business Card</title>
<link rel="stylesheet" href="https://fonts.googleapis.com/css2?family=Michroma&family=Saira+Condensed:wght@300;500&display=swap">
<style>
  :root {
    --page-bg: #e9e9ea;
    --card-bg: #ffffff;
    --band-grey: #6d6d6f;
    --mark-grey: #606062;
    --level-top: #f3cf8a;
    --level-mid: #efb94b;
    --level-low: #c2a874;
    --level-base: #a79b87;
    --name-blue: #1a82d4;
    --email-amber: #f0b840;
    --web-tan: #cfae6c;
    --phone-grey: #d6d6d6;
    --white: #ffffff;
  }
  * { margin: 0; padding: 0; box-sizing: border-box; }
  html, body {
    width: 1200px; height: 708px; overflow: hidden;
    background: var(--page-bg);
  }
  .card {
    position: absolute; left: 60px; top: 65px;
    width: 1080px; height: 578px;
    background: var(--card-bg);
    box-shadow: 0 2px 10px rgba(0,0,0,0.12);
    overflow: hidden;
  }
  .info-band {
    position: absolute; left: 443px; top: 361px;
    width: 637px; height: 217px;
    background: var(--band-grey);
  }
  .level-graphic {
    position: absolute; left: 0; top: 202px;
    width: 442px; height: 376px;
    background: linear-gradient(to bottom,
      var(--level-top) 0%,
      var(--level-mid) 35%,
      var(--level-low) 80%,
      var(--level-base) 100%);
  }

  .brand {
    position: absolute; left: 0; width: 1080px; top: 112px;
    display: flex; justify-content: center; align-items: center; gap: 16px;
  }
  .brand-square { width: 54px; height: 54px; background: var(--mark-grey); }
  .brand-name {
    font-family: "Saira Condensed", sans-serif; font-weight: 500;
    font-size: 50px; line-height: 1; color: var(--email-amber);
  }

  .details {
    position: absolute; right: 93px; top: 365px;
    text-align: right;
  }
  .company {
    font-family: "Michroma", sans-serif; font-size: 34px; line-height: 1.2;
    color: var(--white); font-weight: 400; -webkit-text-stroke: 1px var(--white);
  }
  .person {
    font-family: "Saira Condensed", sans-serif; font-weight: 300;
    font-size: 54px; line-height: 1; color: var(--name-blue);
    margin-top: 4px;
  }
  .contact {
    font-family: "Michroma", sans-serif; font-size: 16.5px; line-height: 25px;
    letter-spacing: 0.5px; margin-top: 8px; list-style: none;
  }
  .contact-email { color: var(--email-amber); }
  .contact-web { color: var(--web-tan); }
  .contact-phone { color: var(--phone-grey); }
</style>
</head>
<body>
  <main class="card">
    <div class="info-band"></div>
    <div class="level-graphic" role="img" aria-label="Decorative amber sound-level graphic"></div>

    <div class="brand">
      <span class="brand-square" aria-hidden="true"></span>
      <span class="brand-name">sound crew</span>
    </div>

    <section class="details">
      <h1 class="company">The Sound Crew</h1>
      <p class="person">Declan Whitford</p>
      <ul class="contact">
        <li class="contact-email">e| declan@thesoundcrewqz.com.au</li>
        <li class="contact-web">w| www.thesoundcrewqz.com.au</li>
        <li class="contact-phone">m| 0412 576 018</li>
      </ul>
    </section>
  </main>
</body>
</html>
```